Business Card Design for high end dental office

Please include attached logo with office name in the font selected for business card design. Emphasis will be on elegance, simplicity with a modern look. We are a high end boutique dental office that focuses on customer service and expertise of our doctors.

The current font chosen for the letters is Garamond, but we are open to suggestions.

The main theme color for the office is cyan and silver.

Target Market(s)

Oral health/esthetics driven adults of the Los Angeles area aged 25 to 80 with above average median household income. Customers range from young professionals such doctors, lawyers, engineers, or entrepreneurs to retired senior citizens.

Industry/Entity Type

Boutique

Colors

Designer to choose colors to be used in the design.

Requirements
Must have
• Business logo and name
Doctor's name and degrees: Marcus Dorval, DDS, MMSc
Doctor's field of work: Smile Solutions/Prosthodontics/Implant Dentistry
Nice to have
• Rounded business card corners.
Background or watermark of logo.
Matte cyan with shiny silver color.
Textured feel.

Files

```html
<!DOCTYPE html>
<html lang="en">
<head>
<meta charset="utf-8">
<title>Crestline Dentistry – Business Card</title>
<link rel="stylesheet" href="https://fonts.googleapis.com/css2?family=EB+Garamond:wght@400;500;600&display=swap">
<style>
  :root {
    --backdrop: #ece9e4;
    --cyan: #1bb6de;
    --cyan-light: #3fd0ef;
    --cyan-deep: #0e9ac2;
    --rule: #1a3c4a;
    --ink: #2d2f33;
    --ink-soft: #3b3e44;
    --brand: #4a4d52;
    --on-silver: #f2f3f4;
  }
  * { box-sizing: border-box; margin: 0; padding: 0; }
  html, body { width: 1200px; height: 1023px; overflow: hidden; }
  body {
    background: var(--backdrop);
    font-family: "EB Garamond", Garamond, Georgia, serif;
    position: relative;
  }
  .card {
    position: absolute;
    width: 580px;
    height: 331px;
    border-radius: 26px;
    overflow: hidden;
    box-shadow: 0 10px 26px rgba(0,0,0,.18);
  }
  .card-front { left: 70px; top: 110px; }
  .card-back { left: 550px; top: 570px;
    background: linear-gradient(160deg, var(--cyan-light), var(--cyan) 55%, var(--cyan-deep)); }
  .card-art { position: absolute; inset: 0; width: 100%; height: 100%; }

  .brand {
    position: absolute; left: 44px; top: 44px;
    display: flex; align-items: center; gap: 18px;
    color: var(--brand);
  }
  .brand-dot {
    width: 64px; height: 64px; border-radius: 50%;
    background: var(--cyan);
  }
  .brand-name { font-size: 40px; font-weight: 500; letter-spacing: 1px; }
  .services {
    position: absolute; left: 0; right: 0; top: 143px;
    text-align: center;
    font-size: 15px; color: var(--on-silver); letter-spacing: .3px;
  }
  .doctor-row {
    position: absolute; left: 24px; right: 24px; top: 178px;
    display: flex; align-items: center; gap: 14px;
  }
  .doctor-row .rule { flex: 1; height: 1px; background: var(--rule); }
  .doctor { font-size: 30px; color: var(--ink); font-weight: 500; white-space: nowrap; }
  .doctor .degrees { font-size: 18px; font-weight: 400; margin-left: 6px; }
  .contact {
    position: absolute; left: 180px; top: 222px;
    font-size: 15px; color: var(--ink-soft); line-height: 1.45;
  }
  .contact b { font-weight: 600; }
  .address {
    position: absolute; right: 40px; bottom: 14px;
    font-size: 14px; color: var(--on-silver); letter-spacing: .4px;
  }
  .back-brand {
    position: absolute; inset: 0;
    display: flex; align-items: center; justify-content: center; gap: 16px;
    color: rgba(40, 70, 90, .45);
  }
  .back-brand .brand-dot { background: rgba(40, 70, 90, .3); width: 50px; height: 50px; }
  .back-brand .brand-name { font-size: 34px; }
</style>
</head>
<body>

<section class="card card-front" aria-label="Business card front">
  <svg class="card-art" viewBox="0 0 580 331" preserveAspectRatio="none" aria-hidden="true">
    <defs>
      <linearGradient id="paperFill" x1="0" y1="0" x2="0" y2="1">
        <stop offset="0" stop-color="#fbfbfb"/>
        <stop offset="1" stop-color="#e9e9e9"/>
      </linearGradient>
      <linearGradient id="cyanFill" x1="0" y1="0" x2="1" y2="1">
        <stop offset="0" stop-color="#3fd0ef"/>
        <stop offset="1" stop-color="#12a6d0"/>
      </linearGradient>
      <linearGradient id="silverFill" x1="0" y1="0" x2="0" y2="1">
        <stop offset="0" stop-color="#a7a9ad"/>
        <stop offset="1" stop-color="#6a6d72"/>
      </linearGradient>
    </defs>
    <rect width="580" height="331" fill="url(#paperFill)"/>
    <rect y="135" width="580" height="196" fill="url(#cyanFill)"/>
    <rect y="135" width="580" height="32" fill="url(#silverFill)"/>
    <path d="M0 331 L0 324 C200 322 340 306 440 278 C500 262 545 256 580 254 L580 331 Z" fill="url(#silverFill)"/>
    <path d="M0 324 C200 322 340 306 440 278 C500 262 545 256 580 254" fill="none" stroke="#dfe1e4" stroke-width="2"/>
  </svg>

  <div class="brand">
    <span class="brand-dot"></span>
    <span class="brand-name">Crestline Dentistry</span>
  </div>
  <p class="services">Smile Solutions | Prosthodontics | Implant Dentistry</p>
  <div class="doctor-row">
    <span class="rule"></span>
    <p class="doctor">Marcus Dorval <span class="degrees">| DDS, MMSc</span></p>
    <span class="rule"></span>
  </div>
  <p class="contact">
    <b>[C]:</b> 555-014-2280<br>
    <b>[E]:</b> mdorval@crestlinedental.com
  </p>
  <p class="address">P.O. Box 412 Fairhaven, OH 43110</p>
</section>

<section class="card card-back" aria-label="Business card back">
  <div class="back-brand">
    <span class="brand-dot"></span>
    <span class="brand-name">Crestline Dentistry</span>
  </div>
</section>

</body>
</html>
```